Brochure Design Project

We are looking for a brochure to communicate the various different program we offer within the "Trail & Habitat Studies" department
( www.fieldtrek.rv82.qz.ca )
We have a large photo bank of students engaged in our programs and can willingly provide them if requested.

Target Market(s)

parents, students, academics, administrators

Industry/Entity Type

Bank

Requirements
Must have
• nature based theme. adventure and ecology.

```html
<!DOCTYPE html>
<html lang="en">
<head>
<meta charset="utf-8">
<title>Trail &amp; Habitat Studies – Program Brochure</title>
<link rel="stylesheet" href="https://fonts.googleapis.com/css2?family=Roboto+Condensed:ital,wght@0,400;0,700;1,400&display=swap">
<style>
  :root{
    --stage:#e7e4de;
    --sky:#1cb3d6;
    --cream:#f8f2dc;
    --orange:#ec7a2c;
    --ink:#2b2b2b;
    --white:#ffffff;
    --stone-light:#c9cbcc;
    --stone-dark:#5d6265;
  }
  *{box-sizing:border-box;margin:0;padding:0}
  html,body{width:1200px;height:1000px;overflow:hidden}
  body{background:var(--stage);font-family:"Roboto Condensed",Arial,sans-serif;color:var(--ink)}
  .brochure{position:absolute;left:40px;top:120px;width:1120px;height:760px;background:var(--sky);overflow:hidden}
  .photo{position:absolute}
  .photo--hands{left:0;top:0;width:370px;height:250px;
    background:linear-gradient(135deg,#e6b48f 0%,#c98a63 45%,#8f5a3c 75%,#6b8f3a 100%);
    clip-path:polygon(0 0,100% 0,100% 55%,78% 100%,0 100%)}
  .photo--boots{left:770px;top:400px;width:340px;height:250px;border-radius:40px 0 0 0;
    background:linear-gradient(160deg,#3c4558 0%,#6a6a70 45%,#c8925a 70%,#8a6a4a 100%)}
  .card{position:absolute;background:var(--cream)}
  .card--left{left:22px;top:306px;width:340px;height:400px;border-radius:30px 30px 0 0}
  .card--middle{left:372px;top:60px;width:350px;height:640px;border-radius:30px 30px 0 0}
  .card--right{left:745px;top:18px;width:360px;height:600px;border-radius:34px 34px 0 0}
  .banner{position:absolute;background:var(--orange);color:var(--white)}
  .banner h2{font-weight:700;line-height:1.05}
  .banner--left{left:30px;top:228px;width:320px;height:66px;padding:9px 16px}
  .banner--left h2{font-size:23px}
  .banner--middle{left:356px;top:40px;width:382px;height:150px;padding:18px 26px}
  .banner--middle h2{font-size:28px}
  .banner--middle .quote{font-style:italic;font-size:14.5px;line-height:1.2;margin-top:4px}
  .banner--right{left:745px;top:72px;width:330px;height:62px;padding:14px 22px}
  .banner--right h2{font-size:26px}
  .copy{position:absolute;font-size:13px;line-height:1.22}
  .copy p{margin:0}
  .copy--left{left:38px;top:322px;width:308px}
  .copy--middle{left:392px;top:206px;width:312px}
  .copy--right{left:768px;top:150px;width:318px}
  .water{position:absolute;left:0;top:640px;width:1120px;height:120px}
  .tab{position:absolute;top:650px;width:66px;height:100px;background:var(--white);border-radius:33px 33px 0 0;
    display:flex;flex-direction:column;align-items:center;justify-content:center;gap:6px;padding:8px 4px;text-align:center}
  .tab__dot{width:14px;height:14px;border-radius:50%;background:var(--orange)}
  .tab__name{font-size:9px;font-weight:700;line-height:1.1;color:var(--ink)}
  .tab--heep{left:300px}
  .tab--cra{left:650px}
  .tab--gat{left:1030px}
</style>
</head>
<body>
<main class="brochure">
  <div class="photo photo--hands" role="img" aria-label="Photo of students joining hands in a team circle"></div>

  <div class="banner banner--left"><h2>Highland Ecology<br>Expedition Program:</h2></div>
  <div class="card card--left"></div>
  <div class="copy copy--left">
    <p>“I have never experienced a sensation like this before and at first, I could not put my finger on what it was, but then I realized it was bliss. ” – Delia (HEEP Alumni)</p>
    <p>“In finding the gifts and potential of others, we discover and unleash a deeper appreciation for ourselves.” – Nora (HEEP Alumni)</p>
    <p>HEEP offers secondary students an applied field-course in Leadership Studies. During this 9-day summer outdoor immersion, students will develop their Action-Centered leadership skills. The climax of HEEP is the Journey, which is taken through a modality of choice (Aboard, Voyageur, SUP). HEEP is a transformative passage where learners develop a deeper relational understanding of themselves within the greater cultural and biological ecology of the Pacific Northwest.</p>
  </div>

  <div class="card card--middle"></div>
  <div class="banner banner--middle">
    <h2>Cedar Ridge Academy:</h2>
    <p class="quote">“Not only was the Cedar Ridge Academy program the most engaging educational experience, it also inspired me to look at my community and our environment in a profoundly new light. – Ben (CRA Alumni)</p>
  </div>
  <div class="copy copy--middle">
    <p>The Cedar Ridge Academy (CRA) is an enriched outdoor education program which focuses on character development through Leadership, Citizenship and Outdoor Adventure. This semester-long program offers students a unique opportunity to obtain high school credits, hard-skills, and outdoor certifications that prepare students for future careers and studies. The program often includes an international service project and a practicum delivering a overnight environmental education program for all grade seven students in the district.</p>
    <p>Panel 3 Green Action Toolbox:</p>
    <p>“Inspiration:&nbsp; It comes to me when I realize that big problems have simple solutions that are within reach and already exist.” – Owen (GAT Alumni)</p>
    <p>The Metro Riverbend Green Action Toolbox is a unique and experience-based youth leadership program that brings together students who are passionate about influencing sustainability in their schools and school communities through action, collaboration, and leadership. This action-packed credit course takes includes a 8 day field camp in August and a number of week-end sessions throughout the fall. The course features a wide range of fun and experiential learning and leadership development opportunities designed to develop the knowledge and skills necessary to take action for sustainability</p>
  </div>

  <div class="card card--right"></div>
  <div class="banner banner--right"><h2>Green Action Toolbox:</h2></div>
  <div class="copy copy--right">
    <p>“Inspiration:&nbsp; It comes to me when I realize that big problems have simple solutions that are within reach and already exist.” – Owen (GAT Alumni)</p>
    <p>The Metro Riverbend Green Action Toolbox is a unique and experience-based youth leadership program that brings together students who are passionate about influencing sustainability in their schools and school communities through action, collaboration, and leadership. This action-packed credit course takes includes a 8 day field camp in August and a number of week-end sessions throughout the fall. The course features a wide range of fun and experiential learning and leadership development opportunities designed to develop the knowledge and skills necessary to take action for sustainability</p>
  </div>
  <div class="photo photo--boots" role="img" aria-label="Photo of students' hiking boots on the trail"></div>

  <svg class="water" viewBox="0 0 1120 120" preserveAspectRatio="none" role="img" aria-label="Photo of rippling stream water">
    <defs>
      <linearGradient id="stream" x1="0" y1="0" x2="0" y2="1">
        <stop offset="0" stop-color="var(--stone-light)"/>
        <stop offset="1" stop-color="var(--stone-dark)"/>
      </linearGradient>
    </defs>
    <path d="M0 55 C120 10 240 20 360 45 C480 72 600 64 720 36 C840 10 960 18 1120 45 L1120 120 L0 120 Z" fill="var(--orange)"/>
    <path d="M0 65 C120 22 240 32 360 57 C480 84 600 76 720 48 C840 22 960 30 1120 57 L1120 120 L0 120 Z" fill="url(#stream)"/>
  </svg>

  <div class="tab tab--heep"><span class="tab__dot"></span><span class="tab__name">HEEP</span></div>
  <div class="tab tab--cra"><span class="tab__dot"></span><span class="tab__name">Cedar Ridge Academy</span></div>
  <div class="tab tab--gat"><span class="tab__dot"></span><span class="tab__name">Green Action Toolbox</span></div>
</main>
</body>
</html>
```